Author needs website header

I want a website header that shows me as an author with a attractive tagline and highlights my new book with a Call to Action to get a Free Chapter

Call

```html
<!DOCTYPE html>
<html lang="en">
<head>
<meta charset="utf-8">
<title>Renata Olawale – Author Header</title>
<link rel="stylesheet" href="https://fonts.googleapis.com/css2?family=Cinzel:wght@500;700&family=Cormorant+Garamond:ital,wght@1,500;1,600&display=swap">
<style>
  :root {
    --sky-edge: #66c8ea;
    --sky-mid: #9ddcf2;
    --sky-glow: #eef9fd;
    --ink-white: #ffffff;
    --ink-green: #1d5a2b;
    --portrait-top: #2a2a33;
    --portrait-mid: #a9a9b4;
    --portrait-low: #d9dde4;
    --book-light: #f7f8f9;
    --book-shade: #cfd6db;
  }
  html, body {
    margin: 0;
    padding: 0;
    overflow: hidden;
    background: #ffffff;
  }
  .header {
    position: relative;
    width: 1200px;
    height: 218px;
    overflow: hidden;
    background:
      radial-gradient(ellipse 420px 260px at 900px 110px, var(--sky-glow) 0%, rgba(238,249,253,0) 100%),
      linear-gradient(90deg, var(--sky-edge) 0%, var(--sky-mid) 45%, #c6ebf8 75%, var(--sky-mid) 100%);
  }
  .offer {
    position: absolute;
    margin: 0;
    color: var(--ink-white);
    font-family: "Cormorant Garamond", Georgia, serif;
    font-style: italic;
    font-weight: 600;
    font-variant: small-caps;
    line-height: 1;
    white-space: nowrap;
  }
  .offer--get { left: 16px; top: 2px; font-size: 50px; }
  .offer--free { left: 54px; top: 50px; font-size: 74px; }
  .offer--chapter { left: 98px; top: 114px; font-size: 96px; }

  .author-portrait {
    position: absolute;
    left: 458px;
    top: 22px;
    width: 142px;
    height: 196px;
    border-radius: 48% 48% 10% 10% / 30% 30% 6% 6%;
    background:
      radial-gradient(ellipse 40px 52px at 50% 32%, var(--portrait-top) 0%, #4b4b55 70%, rgba(75,75,85,0) 100%),
      linear-gradient(180deg, var(--portrait-top) 0%, var(--portrait-mid) 55%, var(--portrait-low) 100%);
    opacity: 0.9;
  }

  .book-promo {
    position: absolute;
    left: 560px;
    top: 46px;
    width: 430px;
    text-align: center;
    color: var(--ink-green);
    font-family: "Cinzel", "Times New Roman", serif;
    line-height: 1;
  }
  .book-promo__label {
    margin: 0;
    font-size: 34px;
    font-weight: 700;
    letter-spacing: 9px;
  }
  .book-promo__title {
    margin: 18px 0 0;
    font-family: "Cormorant Garamond", Georgia, serif;
    font-style: italic;
    font-weight: 500;
    font-variant: small-caps;
    font-size: 40px;
    letter-spacing: 5px;
  }
  .book-promo__by {
    margin: 10px 0 0;
    font-size: 20px;
    font-weight: 500;
    letter-spacing: 3px;
  }
  .book-promo__author {
    margin: 12px 0 0;
    font-size: 27px;
    font-weight: 500;
    letter-spacing: 4px;
  }

  .book-stack {
    position: absolute;
    left: 1056px;
    top: 28px;
    width: 136px;
    height: 184px;
    border-radius: 3px;
    background: linear-gradient(90deg, var(--book-shade) 0%, var(--book-light) 40%, var(--book-light) 100%);
  }
</style>
</head>
<body>
  <header class="header">
    <p class="offer offer--get">Get 1</p>
    <p class="offer offer--free">Free</p>
    <p class="offer offer--chapter">Chapter</p>

    <div class="author-portrait" role="img" aria-label="Portrait photo of author Renata Olawale"></div>

    <div class="book-promo">
      <p class="book-promo__label">NEW BOOK</p>
      <p class="book-promo__title">Call to Action</p>
      <p class="book-promo__by">BY</p>
      <p class="book-promo__author">RENATA OLAWALE</p>
    </div>

    <div class="book-stack" role="img" aria-label="Three copies of the book Hearing the Quiet Voice standing side by side"></div>
  </header>
</body>
</html>
```